Custom LED sign business needs logo and web design.

We need a logo and website design for a new company based in Austin TX. What we do is laser engrave custom artwork for led edge lit signs. Our marketing will be directed to kids rooms, game rooms and business. I would like to see designs that have a neon text effect. The look should feel professional for businesses and fun for kids.

**UPDATE** This website will need a custom design page that uses Quillmark Item Composer type plugin. The users will be able to choose from pre-loaded artwork and fonts or upload there own artwork.
There will also be a ecommerce tab that will. have ready to ship signs available.
Wordpress will be the platform used.

Target Market(s)

Businesses, kids and game rooms

Neon Text effect with logo. Professional but fun.

Logo Text

Vorbrights

Number of Pages Required

5+ page

Font styles to use
Other font styles liked:
• A neon text effect type font. Example picture added

Colors

Designer to choose colors to be used in the design.

Requirements
Must have
• Neon Text effects with a professional tech look. Incorporate the "create", "energize" and "amaze" as the company slogan.
• Quillmark Item Composer for customer interactive sign design.
• Ecommerce platform so that I can upload ready to ship signs.
• Refer to the Create, Energize, Amaze pics attached as company slogan. Use those fonts.
Nice to have
• I would like text to "turn on" when hovered over.
Should not have
• Scattered text locations. Unorganized layout and feel.

```html
<!DOCTYPE html>
<html lang="en">
<head>
<meta charset="utf-8">
<title>Vorbrights — Neon Sign Studio</title>
<link href="https://fonts.googleapis.com/css2?family=Advent+Pro:wght@500;600;700&family=Roboto:wght@400;500&display=swap" rel="stylesheet">
<style>
  :root {
    --stage: #1e232c;
    --page: #1c212a;
    --band: #20252f;
    --footer: #1a1f27;
    --footer-base: #181c24;
    --teal: #22c9d8;
    --teal-soft: rgba(34, 201, 216, 0.35);
    --white: #f2f4f7;
    --muted: #5c6371;
    --dim: #474e5b;
    --field: #2a303b;
    --display: "Advent Pro", sans-serif;
    --body: "Roboto", sans-serif;
  }
  * { margin: 0; padding: 0; box-sizing: border-box; }
  html, body { width: 1200px; height: 2452px; overflow: hidden; }
  body { background: var(--stage); font-family: var(--body); position: relative; }
  .abs { position: absolute; }

  .site { position: absolute; left: 136px; top: 62px; width: 930px; height: 1911px; background: var(--page); box-shadow: 0 0 40px rgba(0,0,0,0.35); }

  /* hero */
  .hero { position: absolute; left: 0; top: 0; width: 930px; height: 491px; overflow: hidden; }
  .hero-visual { position: absolute; inset: 0; background:
      linear-gradient(180deg, rgba(20,26,36,0.55) 0%, rgba(20,26,36,0.2) 40%, rgba(20,26,36,0.6) 100%),
      linear-gradient(180deg, #2a3446 0%, #4a3a48 38%, #6a4a48 48%, #253446 62%, #1a2a34 100%); }
  .brand { position: absolute; font-family: var(--display); font-weight: 600; color: var(--teal); letter-spacing: 1px; }
  .nav { position: absolute; top: 34px; left: 0; font-size: 11px; color: #c4c9d2; font-weight: 500; }
  .nav a { position: absolute; white-space: nowrap; text-decoration: none; color: inherit; }
  .nav a.current { color: var(--teal); }
  .nav a.current::after { content: ""; position: absolute; left: 0; right: 0; top: 22px; height: 2px; background: var(--teal); }
  .cart-count { position: absolute; left: 840px; top: 28px; width: 20px; height: 20px; border: 2px solid var(--teal); border-radius: 50%; color: var(--teal); font-size: 10px; line-height: 16px; text-align: center; }
  .hero-title { position: absolute; left: 130px; top: 170px; font-family: var(--display); font-weight: 600; font-size: 40px; line-height: 51px; color: var(--white); }
  .n1 { color: #e0312b; } .n2 { color: #e3b51a; } .n3 { color: #2f9de0; } .n4 { color: #2fc35a; }
  .btn-neon { position: absolute; border: 2px solid var(--teal); border-radius: 22px; color: var(--teal); font-size: 11px; font-weight: 500; text-align: center; box-shadow: 0 0 10px var(--teal-soft), inset 0 0 8px var(--teal-soft); text-transform: uppercase; }
  .arrow { position: absolute; width: 22px; height: 44px; background: rgba(255,255,255,0.08); }
  .arrow svg { position: absolute; left: 6px; top: 16px; }

  .section-title { position: absolute; left: 0; width: 930px; text-align: center; font-family: var(--display); font-weight: 600; font-size: 25px; color: var(--white); }
  .rule { position: absolute; left: 449px; width: 32px; height: 2px; background: var(--teal); }
  .copy { position: absolute; font-size: 11.5px; line-height: 24.5px; color: var(--muted); }

  /* kids band */
  .kids { position: absolute; left: 0; top: 804px; width: 930px; height: 308px; background: var(--band); }
  .kids-pattern { position: absolute; inset: 0; background: radial-gradient(ellipse at 50% 50%, #232935 0%, #1f242e 100%); }
  .kids-art { position: absolute; left: 212px; top: 69px; width: 138px; height: 157px; background: linear-gradient(180deg, #1e4e58 0%, #191d24 55%, #15181e 100%); border-radius: 4px; }
  .btn-ghost { position: absolute; background: #2c323d; border-radius: 18px; color: #6b7280; font-size: 11px; text-align: center; }

  .thumb { position: absolute; top: 1246px; width: 185px; height: 185px; }

  .newsletter { position: absolute; left: 0; top: 1485px; width: 930px; height: 145px; background: var(--band); }
  .field { position: absolute; left: 426px; top: 54px; width: 330px; height: 31px; background: var(--field); border-radius: 16px; color: #5a616e; font-size: 10px; line-height: 31px; padding-left: 26px; }

  .footer { position: absolute; left: 0; top: 1630px; width: 930px; height: 249px; background: var(--footer); }
  .foot-head { position: absolute; font-size: 11px; color: #6a717e; font-weight: 500; }
  .foot-item { position: absolute; font-size: 10.5px; color: #7a8190; white-space: nowrap; }
  .social { position: absolute; width: 22px; height: 22px; border: 1px solid #3a414d; border-radius: 50%; }
  .footer-base { position: absolute; left: 0; top: 1879px; width: 930px; height: 32px; background: var(--footer-base); }
  .footer-base p { position: absolute; left: 59px; top: 9px; font-size: 9.5px; color: #444b57; }

  .showcase-name { position: absolute; left: 0; width: 1200px; top: 2140px; text-align: center; font-family: var(--display); font-weight: 600; font-size: 150px; line-height: 170px; color: var(--teal); letter-spacing: 4px; }
</style>
</head>
<body>
  <main class="site">
    <header class="hero">
      <div class="hero-visual" role="img" aria-label="Night city skyline photo with a tall angular glass tower at dusk"></div>
      <div class="brand" style="left:59px;top:30px;font-size:34px;">Vorbrights</div>
      <nav class="nav">
        <a class="current" style="left:456px;">Home</a>
        <a style="left:515px;">About us</a>
        <a style="left:591px;">Our services</a>
        <a style="left:685px;">Blog</a>
        <a style="left:737px;">Contact us</a>
      </nav>
      <svg class="abs" style="left:812px;top:31px" width="18" height="16" viewBox="0 0 18 16" fill="none" stroke="#c4c9d2" stroke-width="1.5"><path d="M1 2h3l2 8h9l2-6H5"/><circle cx="7" cy="13.5" r="1.3"/><circle cx="14" cy="13.5" r="1.3"/></svg>
      <div class="cart-count">0</div>
      <h1 class="hero-title">An Aesthetic Artwork Of<br><span class="n1">N</span><span class="n2">e</span><span class="n3">o</span><span class="n4">n</span> Lights</h1>
      <div class="btn-neon" style="left:134px;top:316px;width:124px;height:41px;line-height:37px;">Read more</div>
      <div class="arrow" style="left:0;top:243px;"><svg width="10" height="12" viewBox="0 0 10 12" fill="none" stroke="#c4c9d2" stroke-width="1.5"><path d="M7 1L2 6l5 5"/></svg></div>
      <div class="arrow" style="left:908px;top:243px;"><svg width="10" height="12" viewBox="0 0 10 12" fill="none" stroke="#c4c9d2" stroke-width="1.5"><path d="M3 1l5 5-5 5"/></svg></div>
    </header>

    <section class="about">
      <h2 class="section-title" style="top:530px;">About Us</h2>
      <div class="rule" style="top:574px;"></div>
      <p class="copy" style="left:0;width:930px;top:601px;text-align:center;">Lorem Ipsum is simply dummy text of the printing and typesetting industry. Lorem Ipsum has been the<br>industry's standard dummy text ever since the 1500s, when an unknown printer took a galley of type and<br>scrambled it to make a type specimen book.</p>
      <div class="btn-neon" style="left:415px;top:711px;width:100px;height:33px;line-height:29px;font-size:10px;">Read more</div>
    </section>

    <section class="kids">
      <div class="kids-pattern" role="img" aria-label="Faint line doodle pattern of toys and kids' room items"></div>
      <div class="kids-art" role="img" aria-label="Illustration of a baby crib with a glowing neon mobile of moon and stars"></div>
      <h3 class="abs" style="left:405px;top:48px;font-family:var(--display);font-weight:600;font-size:23px;color:var(--white);">Kids Rooms</h3>
      <p class="copy" style="left:405px;top:91px;width:340px;font-size:11px;line-height:20.5px;">It is a long established fact that a reader will be distracted by the readable content of a page when looking at its layout. The point of using Lorem Ipsum is that it has a more-or-less normal distribution of letters, as opposed to using 'Content here, content here', making it look like readable English.</p>
      <div class="btn-ghost" style="left:407px;top:211px;width:121px;height:35px;line-height:35px;">VIEW PROJECTS</div>
      <svg class="abs" style="left:115px;top:148px" width="10" height="14" viewBox="0 0 10 14" fill="none" stroke="#6b7280" stroke-width="1.5"><path d="M8 1L2 7l6 6"/></svg>
      <svg class="abs" style="left:801px;top:148px" width="10" height="14" viewBox="0 0 10 14" fill="none" stroke="#6b7280" stroke-width="1.5"><path d="M2 1l6 6-6 6"/></svg>
    </section>

    <section class="projects">
      <h2 class="section-title" style="top:1160px;">Recent Projects</h2>
      <div class="rule" style="top:1207px;"></div>
      <div class="thumb" style="left:59px;background:linear-gradient(160deg,#3a2410,#c98a12 50%,#2a1a0c);" role="img" aria-label="Photo of a gold neon Happy Birthday sign"></div>
      <div class="thumb" style="left:266px;background:linear-gradient(160deg,#0c3a12,#38e040 50%,#123a16);" role="img" aria-label="Photo of a green neon graffiti lettering sign"></div>
      <div class="thumb" style="left:474px;background:linear-gradient(160deg,#4a0c10,#e2323a 50%,#5a0e12);" role="img" aria-label="Photo of a red neon sign with a numbered ball"></div>
      <div class="thumb" style="left:682px;background:linear-gradient(160deg,#7a1a8a,#e43ad8 50%,#b020c0);" role="img" aria-label="Photo of a pink neon script word sign"></div>
    </section>

    <section class="newsletter">
      <h3 class="abs" style="left:104px;top:32px;font-family:var(--display);font-weight:600;font-size:23px;color:var(--white);">Signup Newsletter</h3>
      <p class="copy" style="left:113px;top:68px;font-size:10px;line-height:21px;color:var(--dim);">It is a long established fact that a reader will be distracted<br>by the readable content.</p>
      <div class="field">Enter Your Email Address</div>
      <div class="btn-neon" style="left:739px;top:50px;width:108px;height:36px;line-height:32px;font-size:10px;background:var(--field);">Subscribe</div>
    </section>

    <footer class="footer">
      <div class="foot-head" style="left:59px;top:62px;">Quick Navigation</div>
      <div class="foot-item" style="left:59px;top:92px;">Home</div>
      <div class="foot-item" style="left:59px;top:116px;">About Us</div>
      <div class="foot-item" style="left:59px;top:140px;">Order Information</div>
      <div class="foot-item" style="left:59px;top:164px;">Specifications</div>
      <div class="foot-item" style="left:59px;top:188px;">Contacts us</div>

      <div class="foot-head" style="left:248px;top:62px;">Support</div>
      <div class="foot-item" style="left:248px;top:92px;">FAQS</div>
      <div class="foot-item" style="left:248px;top:116px;">Sitemap</div>
      <div class="foot-item" style="left:248px;top:140px;">Terms &amp; Conditions</div>

      <div class="foot-head" style="left:467px;top:62px;">Contact us</div>
      <div class="foot-item" style="left:467px;top:94px;">Cedar Lane (B45), Hollowmere,</div>
      <div class="foot-item" style="left:467px;top:115px;">Westvale HM4 220</div>
      <svg class="abs" style="left:467px;top:139px" width="10" height="10" viewBox="0 0 10 10" fill="#7a8190"><path d="M2 0.5l2 2-1 1.3a6 6 0 003.2 3.2l1.3-1 2 2-1.2 1.5C4.5 9.5 0.5 5.5 0.5 1.7z"/></svg>
      <div class="foot-item" style="left:482px;top:137px;">CALL: +12 555 0142</div>
      <svg class="abs" style="left:467px;top:161px" width="11" height="10" viewBox="0 0 11 10" fill="#7a8190"><rect x="0" y="3" width="11" height="6" rx="1"/><rect x="2.5" y="0" width="6" height="3"/></svg>
      <div class="foot-item" style="left:482px;top:160px;">FAX: +12 555 0143</div>
      <svg class="abs" style="left:467px;top:183px" width="11" height="8" viewBox="0 0 11 8" fill="none" stroke="#7a8190"><rect x="0.5" y="0.5" width="10" height="7"/><path d="M0.5 0.5l5 4 5-4"/></svg>
      <div class="foot-item" style="left:482px;top:181px;">Email: info@glowmere.example</div>

      <div class="brand" style="left:710px;top:70px;font-size:30px;">Vorbrights</div>
      <div class="social" style="left:713px;top:162px;"></div>
      <div class="social" style="left:747px;top:162px;"></div>
      <div class="social" style="left:782px;top:162px;"></div>
    </footer>
    <div class="footer-base"><p>Glowmere Studio. All rights reserved</p></div>
  </main>

  <div class="showcase-name">Vorbrights</div>
</body>
</html>
```